FOOD PACKAGING DESIGN FOR TRIVELLO KITCHENS - BRIEF UPDATED..

Hello Everyone

After discussions with Makerfold and the amount of work on this project, we have decided to split this project into phase 1 and phase 2 to make it more fair.

The allocated design budget is for Phase 1 only but we have included phase 2 below so you see the long term vision on this.

Phase 1 are products which we would like immediate designs on, once a winner is selected we will agree a fee with the designer via makerfold and design phase 2 products too.

This will ensure a reasonable number of designs for each phase.

After the successful design of a logo on makerfold, this is a packaging design project for Trivello Kitchens‎.

Initially this is not guaranteed as on a couple of occasions in the past we have been disappointed with the response but as soon as we receive a couple of designs that we believe we can take live, IMMEDIATELY WE WILL PAYMENT GUARANTEE THIS PROJECT, WITHOUT ANY HESITATION AND THIS IS NOT OUR FIRST PROJECT ON MAKERFOLD, PAYMENT HAS ALREADY BEEN MADE TO MAKERFOLD, IT IS JUST A MATTER OF RECEIVING SOME GOOD DESIGNS NOW AND WE’LL GUARANTEE IT.

This will be a big design project so we only want designers that can work with us on this long term.

We are a frozen food manufacturer and wholesaler and we are now looking to launch a retail brand under the name Trivello Kitchens, you can find more information about our company and what we sell by visiting our main website www.glaciermarten.example .

All the packaging we design will be for frozen food packaging.

The packaging will be frozen food bags and also folding carton boxes.

PHASE 1 BAGS:

Samosas:

1. 10, 20 and 50 Pack Meat ‎Samosas – One design but 3 pack sizes for all.
2. 10, 20 and 50 Pack Chicken Samosas
3. 10, 20 and 50 Pack Vegetable Samosas
4. 10, 20 and 50 Pack Chicken Tikka Samosas

Spring Rolls:

5. 10, 20 and 50 Pack Meat Spring Rolls – Again, one design but 3 pack sizes.
6. 10, 20 and 50 Pack Chicken Spring Rolls
7. 10, 20 and 50 Pack Vegetable Spring Rolls
8. 10, 20 and 50 Pack Chicken Tikka Spring Rolls

Seekh Kebabs:

9. 10 and 20 Pack Meat Seekh Kebabs – Ready Cooked (small writing not heading).
10. 10 and 20 Pack Chicken Seekh Kebabs – Ready Cooked (small writing not heading).

Chapli Kebabs:

11. Meat Chapli Kebabs, 8 Pack (500g) – Ready Cooked (small writing not heading).
12. Chicken Chapli Kebabs, 8 Pack (500g) – Ready Cooked (small writing not heading).

Doners and Shawarma Kebabs:

13. Cooked, Sliced, Traditional Doner Kebab – 1kg

Sausages:

14. 10 and 20 Pack Lamb Sausages
15. 10 and 20 Pack Beef Sausages
16. 10 and 20 Pack Chicken Sausages

Coated Chicken Range:

17. 750g and 1kg Battered Chicken Nuggets
18. 750g and 1kg‎ Breaded Chicken Nuggets

19. 750g and 1kg Battered Chicken Pops
20. 750g and 1kg‎ Breaded Chicken Pops

21. 750g and 1kg Battered Chicken Goujon Strips

22. 750g and 1kg‎ Breaded Chicken Goujon Strips

23. 10 Battered Chicken Burgers – Approx 850g
24. 10 Breaded Chicken Burgers – Approx 850g
25. 10 Southern Fried Chicken Burgers – Approx 850g

26. 1kg Battered Chicken Wings
27. 1kg Breaded Chicken Wings

BOXES – FOLDING CARTONS – PHASE 1:

Boxes will be as follows:

Burgers:

1. 8 Pack - Beef Burgers
2. 8 Pack - Chicken Burgers
3. 8 Pack - Lamb Burgers

PHASE 2 BAGS:

Shami Kebabs:

1. Meat Shami Kebabs, 8 Pack (500g) – Ready Cooked (small writing not heading).
2. Chicken Shami Kebabs‎, 8 Pack (500g) – Ready Cooked (small writing not heading).

1. Cooked, Sliced, Plain Chicken Shawarma – 1 kg
2. Cooked, Sliced, Tandoori Chicken Shawarma – 1 kg
3. Cooked, Sliced, Chicken Tikka Shawarma – 1 kg

Chicken Wings:

1. 1kg Hot & Spicy Chicken Wings
2. 1kg BBQ Chicken Wings
3. 1kg Peri Peri Chicken Wings
4. 1kg Tandoori Chicken Wings

At this stage we are looking for the design ideas and we’ll confirm the exact bag size when we select the final winner, here are some size guidelines:

• 10 Pack Bag Size – Length 23cm x Width 23cm
• 20 Pack Bag Size – Length 29cm x Width 24cm
• 50 Pack Bag Size – Length 34cm x Width 31cm
• 500g Bag Size – Length 27cm x Width 24cm
• 750g Bag Size – Length 29cm x Width 24cm
• 1kg Bag Size – Length 31cm x Width 27cm

BOXES – FOLDING CARTONS – PHASE 2:

Boxes will be as follows:

Seekh Kebabs:

1. 10 Pack and 20 Pack Lamb Seekh Kebabs – Ready Cooked (small writing not heading).

2. 10 Pack and 20 Pack Chicken Seekh Kebabs – Ready Cooked (small writing not heading).

Sausages:

3. 10 Pack Lamb Sausages
4. 10 Pack Beef Sausages
5. 10 Pack Chicken Sausages

6. 10 Pack Lamb Sausage Rolls
7. 10 Pack Beef Sausage Rolls
8. 10 Pack Chicken Sausage Rolls

Pies:

9. Chicken & Mushroom Pie – 12cm Length x 12cm Width x 4cm Depth
10. Chicken Tikka Pie – 12cm Length x 12cm Width x 5cm Depth
11. Steak & Kidney Pie – 12cm Length x 12cm Width x 4cm Depth
12. Meat & Onion Pie – 12cm Length x 12cm Width x 4cm Depth
13. Meat & Potato Pie – 12cm Length x 12cm Width x 5.5cm Depth

Pasties:

14. Chicken Tikka Pasty – 12cm Length x 12cm Width x 5cm Depth
15. Chicken & Sweetcorn Pasty – 12cm Length x 12cm Width x 5cm Depth
16. Keema Pasty – 12cm Length x 12cm Width x 5cm Depth

Ready Meals:

16cm Length x 16cm Width x 5cm

17. Lasagne
18. Chicken Curry & Rice
19. Chicken Tikka Masala & Rice
20. Butter Chicken & Rice
21. Chicken Jalfrezi & Rice
22. Chicken Saag & Rice
23. Lamb Curry & Rice
24. Lamb Rogan Josh & Rice
25. Daal Makhni & Rice
26. Mattar Paneer & Rice

Box Sizes:

• 10 Pack Box – Length 12cm x Width 25cm x Depth 5cm
• 20 Pack Box – To be Confirmed.
• Ready Meals - 16cm Length x 16cm Width x 5cm

The packaging that is designed must be clean and crisp with a classy premium feel to it, see the attached examples or email us for more ideas of what we like.

18. https://www.pinboardly.example/pin/100000000000000001/
19. https://www.pinboardly.example/pin/1000000000000002/
20. https://www.pinboardly.example/pin/100000000000000003/
21. https://www.pinboardly.example/pin/10000000000000004/
22. https://www.pinboardly.example/pin/1000000000000005/
23. https://www.pinboardly.example/pin/100000000000000006/
24. https://www.pinboardly.example/pin/100000000000000007/
25. https://www.pinboardly.example/pin/100000000000000008/
26. https://vellumgreens.example/products/
27. http://www.boxcritic.example/blog/2017/4/4/norvik-creamery-updated-packaging-now-features-a-mosaic-of-taste
28. https://www.pinboardly.example/pin/100000000000000009/
29. https://www.pinboardly.example/pin/100000000000000010/
30. https://www.folioweave.example/gallery/1000011/TONIC-WRAPPER
31. https://www.pinboardly.example/pin/100000000000000012/
32. https://www.pinboardly.example/pin/100000000000000013/
33. https://www.pinboardly.example/pin/100000000000000014/
34. https://www.pinboardly.example/pin/100000000000000015/

Our Competitors:

To help the designers, we have enclosed some links below of what our competitors are doing and how their packaging is designed, please note we don’t want anyone to copy their designs, ideas or styles, we are looking for something original but these links are given to help you so you can see what others are doing in our industry:

• http://dorvantfoods.example/products/ - Samosas, Spring Rolls, Kebabs etc, Bags
• http://www.plx-eats.example/ - Burgers, Sausages, Kebabs etc, folding cartons.
• http://tastewharf.example/assets/product-catalogue-2016.pdf - all foods
• https://cobaltlane.example/frozen-meals/ - ready meals

The packaging will have the following details on it:

1. Images of products for example sausages, burgers, chicken nuggets etc.

2. Quantity per pack - Front

3. Weight per pack – Front or Back.

4. Bar code – Back – to be provided for each item once winner is selected.

5. Halal logo at front‎.

6. Ingredients - Back

7. Possibly multilingual ingredients - Back, English, French, German etc.

8. Cooking instructions – Back.

9. Nutritional information table - Back.

10. Factory health mark of where the product is manufactured - Back

11. Contact details stating, "Trivellos is a Glacier Marten brand", followed by contact details, Tel: +44 (0) 800 555 0147, hello@glaciermarten.example, www.glaciermarten.example, www.trivellokitchens.example

We have attached some images of samosas, spring rolls, burgers, kebabs, pies and pasties etc to help with the design but you don’t have to use these images you can select your own at the initial stage, if we don’t like the image, we will provide these or we’ll select from picvault, frame depot etc.

The winning Trivello Kitchens Logo from Makerfold has been attached.

Glacier Marten (parent company logo) has also been attached so it can be used on the back of each packaging.

This will be an ongoing project where there will be regular work for the designer that is selected as the brand grows and we add more products to the brand.

Initially we are just looking for ideas on the packaging design but once finalised we would need it adjusted to the correct print size and resolution.

Thank you and we look forward to receiving your packaging ideas.

Glacier Marten

Food and drink industry, general public, halal market, Muslim customer base.

• Please read brief.
• Please read brief.

```html
<!DOCTYPE html>
<html lang="en">
<head>
<meta charset="utf-8">
<title>Trivello Kitchens – Samosa Range</title>
<link rel="stylesheet" href="https://fonts.googleapis.com/css2?family=Open+Sans:wdth,wght@75..100,400..800&display=swap">
<style>
  :root {
    --canvas-bg: #f3f3f3;
    --bag-white: #ffffff;
    --ink: #2b2b2b;
    --brand-blue: #2a3a9c;
    --meat-orange: #f08a3a;
    --meat-band: #f4a15a;
    --meat-band-light: #f9c697;
    --chicken-red: #e8444a;
    --chicken-band: #ec5a58;
    --chicken-band-light: #f48d86;
    --veg-lime: #a3c846;
    --veg-band: #1f5630;
    --veg-band-light: #3f7a45;
    --keep-red: #e53935;
    --keep-lime: #a6c94a;
    --badge-green: #1d6436;
    --badge-green-light: #2f8a4d;
    --food-gold: #e2a94e;
    --food-plate: #f4f1ea;
  }
  * { box-sizing: border-box; margin: 0; padding: 0; }
  html, body { width: 1200px; height: 597px; overflow: hidden; }
  body {
    background: var(--canvas-bg);
    font-family: "Open Sans", Arial, sans-serif;
    color: var(--ink);
    position: relative;
  }
  .pack {
    position: absolute;
    top: 50px;
    width: 324px;
    height: 506px;
    background: var(--bag-white);
    border-radius: 6px;
    box-shadow: 0 1px 3px rgba(0,0,0,.08);
  }
  .pack--meat { left: 32px; --flavour: var(--meat-orange); --band: var(--meat-band); --band-light: var(--meat-band-light); --keep: var(--keep-red); }
  .pack--chicken { left: 396px; --flavour: var(--chicken-red); --band: var(--chicken-band); --band-light: var(--chicken-band-light); --keep: var(--keep-lime); }
  .pack--veg { left: 808px; --flavour: var(--veg-lime); --band: var(--veg-band); --band-light: var(--veg-band-light); --keep: var(--keep-red); }

  .brand {
    position: absolute;
    top: 98px; left: 0; width: 100%;
    display: flex; align-items: center; justify-content: center; gap: 6px;
    font-size: 15px; font-weight: 600;
    color: var(--brand-blue);
  }
  .brand__dot {
    width: 10px; height: 10px; border-radius: 50%;
    background: var(--brand-blue);
  }
  .flavour {
    position: absolute;
    top: 182px; left: 0; width: 100%;
    text-align: center;
    font-size: 31px; font-weight: 600;
    font-stretch: 75%;
    color: var(--flavour);
    line-height: 1;
  }
  .product {
    position: absolute;
    top: 210px; left: 0; width: 100%;
    text-align: center;
    font-size: 46px; font-weight: 600;
    letter-spacing: 1px;
    line-height: 1;
  }
  .serving {
    position: absolute;
    top: 282px; left: 48px;
    width: 228px; height: 94px;
  }
  .band {
    position: absolute;
    top: 382px; left: 24px;
    width: 278px; height: 61px;
    background:
      radial-gradient(ellipse at 30% 50%, var(--band-light) 0%, transparent 60%),
      radial-gradient(ellipse at 78% 50%, var(--band-light) 0%, transparent 55%),
      var(--band);
  }
  .keep-frozen {
    position: absolute;
    top: 366px; left: 39px;
    width: 47px; height: 47px;
    background: var(--keep);
    color: #fff;
    border-radius: 2px;
    display: flex; flex-direction: column; justify-content: center; align-items: center;
    line-height: 1.05;
  }
  .keep-frozen__big { font-size: 12px; font-weight: 700; }
  .keep-frozen__small { font-size: 10px; font-weight: 600; }
  .count {
    position: absolute;
    top: 429px; left: 199px;
    width: 34px; height: 34px; border-radius: 50%;
    background: var(--badge-green);
    border: 2px solid #fff;
    color: #fff;
    display: flex; flex-direction: column; align-items: center; justify-content: center;
    line-height: 1;
  }
  .count__num { font-size: 13px; font-weight: 700; }
  .count__label { font-size: 5px; font-weight: 600; }
  .cert {
    position: absolute;
    top: 429px; left: 240px;
    width: 34px; height: 34px; border-radius: 50%;
    background: radial-gradient(circle at 50% 40%, var(--badge-green-light), var(--badge-green) 70%);
    border: 2px solid #fff;
    box-shadow: inset 0 0 0 3px var(--badge-green), inset 0 0 0 4px rgba(255,255,255,.85);
  }
  .net-weight {
    position: absolute;
    top: 464px; left: 0; width: 100%;
    text-align: center;
    font-size: 10px; font-weight: 600;
  }
</style>
</head>
<body>
  <section class="pack pack--meat">
    <div class="brand"><span class="brand__dot"></span>Trivello Kitchens</div>
    <div class="flavour">MEAT</div>
    <div class="product">SAMOSA</div>
    <svg class="serving" viewBox="0 0 228 94" role="img" aria-label="Meat samosas on a white plate with chives">
      <defs><radialGradient id="food-meat" cx="50%" cy="45%" r="55%"><stop offset="0" stop-color="var(--food-gold)"/><stop offset="1" stop-color="var(--food-plate)"/></radialGradient></defs>
      <ellipse cx="114" cy="52" rx="112" ry="40" fill="url(#food-meat)"/>
    </svg>
    <div class="band" role="img" aria-label="Geometric star pattern band in orange"></div>
    <div class="keep-frozen"><span class="keep-frozen__big">KEEP</span><span class="keep-frozen__small">Frozen</span></div>
    <div class="count"><span class="count__num">20</span><span class="count__label">per pack</span></div>
    <div class="cert" role="img" aria-label="Halal certification mark"></div>
    <div class="net-weight">NET.WT. 7 OZ (125g)</div>
  </section>

  <section class="pack pack--chicken">
    <div class="brand"><span class="brand__dot"></span>Trivello Kitchens</div>
    <div class="flavour">CHICKEN</div>
    <div class="product">SAMOSA</div>
    <svg class="serving" viewBox="0 0 228 94" role="img" aria-label="Chicken samosas on a white plate with salad">
      <defs><radialGradient id="food-chicken" cx="50%" cy="45%" r="55%"><stop offset="0" stop-color="var(--food-gold)"/><stop offset="1" stop-color="var(--food-plate)"/></radialGradient></defs>
      <ellipse cx="114" cy="50" rx="112" ry="43" fill="url(#food-chicken)"/>
    </svg>
    <div class="band" role="img" aria-label="Geometric star pattern band in red"></div>
    <div class="keep-frozen"><span class="keep-frozen__big">KEEP</span><span class="keep-frozen__small">Frozen</span></div>
    <div class="count"><span class="count__num">20</span><span class="count__label">per pack</span></div>
    <div class="cert" role="img" aria-label="Halal certification mark"></div>
    <div class="net-weight">NET.WT. 7 OZ (125g)</div>
  </section>

  <section class="pack pack--veg">
    <div class="brand"><span class="brand__dot"></span>Trivello Kitchens</div>
    <div class="flavour">VEGETABLE</div>
    <div class="product">SAMOSA</div>
    <svg class="serving" viewBox="0 0 228 94" role="img" aria-label="Vegetable samosas on a white plate with peppers">
      <defs><radialGradient id="food-veg" cx="50%" cy="45%" r="55%"><stop offset="0" stop-color="var(--food-gold)"/><stop offset="1" stop-color="var(--food-plate)"/></radialGradient></defs>
      <ellipse cx="114" cy="48" rx="112" ry="44" fill="url(#food-veg)"/>
    </svg>
    <div class="band" role="img" aria-label="Geometric star pattern band in dark green"></div>
    <div class="keep-frozen"><span class="keep-frozen__big">KEEP</span><span class="keep-frozen__small">Frozen</span></div>
    <div class="count"><span class="count__num">20</span><span class="count__label">per pack</span></div>
    <div class="cert" role="img" aria-label="Halal certification mark"></div>
    <div class="net-weight">NET.WT. 7 OZ (125g)</div>
  </section>
</body>
</html>
```